Business card design needed

The company name is Pellwick Architects. We are an architectural company based in Melbourne,Australia that has a mix of client base from health care, commercial office, aged care, multi-residential, single residential and retail. Design type is contemporary.

Suggest the base colours need to be black and white. Please leave an area on the back of the card available for handwritten notes.

Target Market(s)

Generally corporate, aged 30 to 65

Industry/Entity Type

Residential

Contact Information for Business Card

Pellwick Architects
Dane Pellwick
7 Horbury Street
Northvale VIC 3059
T (03) 9572 4016
M 0431 607 295
E dp@pellwickarc.com.au

Logo Text

PA

Logo styles of interest
Emblem Logo
Abstract Logo
Lettermark Logo
Requirements
Must have
• I am having trouble attaching a sketch so would really appreciate your effort to try the following brief.

Black and White (B&W)
Would like different card cutout profile. Logo Example, use the half circle curve of the G to form the left edge of the card with no margin. The A is to sit inside the G, connected to the G by its horizontal. The A has its cross bar and lower right leg removed. Card in black, text in white.

Back of card to be black text on white background with services provided.

Client Focused Service
Architecture and Design
Functional Planning
Town Planning
Feasability Studies
Contract Documentation
Contract Administration
Project Management

Simple elegant text, Ariel or similar
Nice to have
• Integrated logo and card cut-out.

Card base black on front, white on back
Should not have
• Too many colours
Fussy details

```html
<!DOCTYPE html>
<html lang="en">
<head>
<meta charset="utf-8">
<title>Pellwick Architects – Business Card</title>
<link href="https://fonts.googleapis.com/css2?family=Arimo:wght@400;700&display=swap" rel="stylesheet">
<style>
  :root {
    --backdrop: #5e5e5e;
    --card-black: #1c1c1c;
    --card-white: #ffffff;
    --ink-white: #ffffff;
    --ink-grey: #4a4a4a;
    --rule-grey: #8a8a8a;
    --rule-light: #9a9a9a;
  }
  * { margin: 0; padding: 0; box-sizing: border-box; }
  html, body {
    width: 1200px;
    height: 850px;
    overflow: hidden;
    background: var(--backdrop);
    font-family: "Arimo", Arial, sans-serif;
  }
  .canvas {
    position: relative;
    width: 1200px;
    height: 850px;
  }
  .card {
    position: absolute;
    left: 290px;
    width: 620px;
    height: 378px;
  }

  /* Front */
  .card-front {
    top: 27px;
    background: var(--card-black);
    color: var(--ink-white);
    border-radius: 189px 0 0 189px;
  }
  .front-rule {
    position: absolute;
    top: 14px;
    right: 26px;
    width: 2px;
    height: 270px;
    background: var(--rule-grey);
  }
  .contact {
    position: absolute;
    top: 130px;
    right: 40px;
    text-align: right;
    font-size: 16px;
    line-height: 21px;
  }
  .contact .person {
    font-weight: 700;
    font-size: 16px;
    margin-bottom: 24px;
  }
  .brand-name {
    position: absolute;
    right: 22px;
    bottom: 14px;
    font-size: 40px;
    font-weight: 400;
    letter-spacing: -0.5px;
    color: var(--ink-white);
  }
  .brand-disc {
    position: absolute;
    left: 60px;
    top: 66px;
    width: 140px;
    height: 140px;
    border-radius: 50%;
    background: var(--ink-white);
  }

  /* Back */
  .card-back {
    top: 445px;
    background: var(--card-white);
    border-radius: 0 0 120px 0;
  }
  .back-brand {
    position: absolute;
    left: 26px;
    top: 110px;
    width: 130px;
    text-align: center;
  }
  .back-disc {
    display: block;
    width: 96px;
    height: 96px;
    margin: 0 auto 18px;
    border-radius: 50%;
    background: var(--ink-grey);
  }
  .back-name {
    font-size: 14px;
    color: var(--ink-grey);
  }
  .back-rule {
    position: absolute;
    left: 170px;
    top: 10px;
    width: 2px;
    height: 352px;
    background: var(--rule-light);
  }
  .services {
    position: absolute;
    left: 186px;
    top: 16px;
    list-style: none;
    font-size: 19px;
    line-height: 43.5px;
    color: var(--ink-grey);
  }
  .notes-area {
    position: absolute;
    right: 0;
    top: 0;
    width: 200px;
    height: 100%;
  }
</style>
</head>
<body>
<main class="canvas">
  <section class="card card-front" aria-label="Card front">
    <span class="brand-disc" aria-hidden="true"></span>
    <div class="front-rule"></div>
    <address class="contact">
      <p class="person">Dane Pellwick</p>
      <p>7 Horbury Street</p>
      <p>Northvale VIC 3059</p>
      <p>T (03) 9572 4016</p>
      <p>M 0431 607 295</p>
      <p>E dp@pellwickarc.com.au</p>
    </address>
    <p class="brand-name">Pellwick Architects</p>
  </section>

  <section class="card card-back" aria-label="Card back">
    <div class="back-brand">
      <span class="back-disc" aria-hidden="true"></span>
      <p class="back-name">Pellwick Architects</p>
    </div>
    <div class="back-rule"></div>
    <ul class="services">
      <li>Client Focused Service</li>
      <li>Architecture and Design</li>
      <li>Functional Planning</li>
      <li>Town Planning</li>
      <li>Feasability Studies</li>
      <li>Contract Documentation</li>
      <li>Contract Administration</li>
      <li>Project Management</li>
    </ul>
    <div class="notes-area" aria-label="Space for handwritten notes"></div>
  </section>
</main>
</body>
</html>
```